Civic Holdwell Business Card

We are looking to design new business cards for our company. We have two office locations and would like to have both full addresses on the card. Each address needs two lines for the building name and street address and a line or two for the city, state and zip code. There should be a place for 2-3 phone numbers. The addresses and phone numbers are at the bottom of this description. We also need a place to put our company website and one email address. Our logo is attached.
We would like the card to be two sided. The back of the card should have a blue background with some part of our logo design on it. We would like the full logo on the front of the card as well. The front of the card should have a white background with the blue logo. We are open to listing our addresses on the front or the back of the card. The person who designed our logo gave us an excellent business card idea that we really liked. I have attached a picture of his business card idea so that we can build off of it.
Addresses:
The Tanner Hall
2184 17th Street NW
Washington, DC 20007
Marlow Crest Tower
410 Dorsen Avenue #2215
Miami, FL 33131
Phone Numbers: (202) 555-0148
(202) 555-0193
Website: www.civicholdwell.example

```html
<!DOCTYPE html>
<html lang="en">
<head>
<meta charset="utf-8">
<title>Civic Holdwell Business Card</title>
<link rel="stylesheet" href="https://fonts.googleapis.com/css2?family=Source+Sans+3:wght@400&display=swap">
<style>
  :root {
    --backdrop: #8c837d;
    --card-blue: #2f40a3;
    --logo-navy: #1f2a6e;
    --card-cream: #e7ddc6;
    --ink-white: #f4f4f8;
    --hole: #8c837d;
  }
  * { box-sizing: border-box; margin: 0; padding: 0; }
  html, body {
    width: 1200px; height: 864px; overflow: hidden;
    background: var(--backdrop);
    font-family: "Source Sans 3", Arial, sans-serif;
    font-weight: 400;
  }
  .card-sheet {
    position: relative; width: 1200px; height: 864px;
    display: flex; align-items: center; justify-content: center; gap: 50px;
  }
  .card {
    position: relative; width: 525px; height: 300px;
    box-shadow: 0 6px 18px rgba(0,0,0,0.25);
  }
  /* Front */
  .card-front { background: var(--card-cream); color: var(--logo-navy); }
  .card-front .punch-hole {
    position: absolute; right: 22px; top: 50%; width: 16px; height: 16px;
    margin-top: -8px; border-radius: 50%; background: var(--hole);
  }
  .brand { display: flex; align-items: center; gap: 14px; }
  .brand-square { flex: none; border-radius: 8px; }
  .brand-name { display: flex; flex-direction: column; line-height: 1; text-transform: uppercase; }
  .card-front .brand { position: absolute; left: 50px; top: 96px; }
  .card-front .brand-square { width: 96px; height: 96px; background: var(--logo-navy); }
  .card-front .brand-primary { font-size: 64px; letter-spacing: 1px; }
  .card-front .brand-secondary { font-size: 34px; letter-spacing: 10px; margin-top: 4px; }
  /* Back */
  .card-back { background: var(--card-blue); color: var(--ink-white); }
  .card-back .brand { position: absolute; left: 0; right: 0; top: 22px; justify-content: center; gap: 10px; }
  .card-back .brand-square { width: 52px; height: 52px; background: var(--ink-white); border-radius: 6px; }
  .card-back .brand-primary { font-size: 34px; letter-spacing: 1px; }
  .card-back .brand-secondary { font-size: 18px; letter-spacing: 6px; margin-top: 2px; }
  .rule {
    position: absolute; left: 46px; right: 46px; height: 0;
    border-top: 2px dotted var(--ink-white);
  }
  .rule-top { top: 90px; }
  .rule-bottom { top: 140px; }
  .phones {
    position: absolute; left: 0; right: 0; top: 102px;
    display: flex; justify-content: center; gap: 28px;
    font-size: 20px; line-height: 26px; letter-spacing: 1px;
  }
  .addresses {
    position: absolute; left: 30px; top: 154px;
    display: flex; gap: 40px;
  }
  .address {
    font-size: 14px; line-height: 20px; font-style: normal;
  }
  .web-contact {
    position: absolute; right: 36px; bottom: 18px;
    text-align: right; font-size: 14px; line-height: 20px;
  }
</style>
</head>
<body>
<main class="card-sheet">
  <section class="card card-front" aria-label="Card front">
    <div class="brand">
      <span class="brand-square" aria-hidden="true"></span>
      <span class="brand-name">
        <span class="brand-primary">Civic</span>
        <span class="brand-secondary">Holdwell</span>
      </span>
    </div>
    <span class="punch-hole" aria-hidden="true"></span>
  </section>

  <section class="card card-back" aria-label="Card back">
    <div class="brand">
      <span class="brand-square" aria-hidden="true"></span>
      <span class="brand-name">
        <span class="brand-primary">Civic</span>
        <span class="brand-secondary">Holdwell</span>
      </span>
    </div>
    <span class="rule rule-top" aria-hidden="true"></span>
    <p class="phones">
      <span class="phone">(202) 555-0148</span>
      <span class="phone">(202) 555-0193</span>
    </p>
    <span class="rule rule-bottom" aria-hidden="true"></span>
    <div class="addresses">
      <address class="address">
        The Tanner Hall<br>
        2184 17th Street NW<br>
        Washington, DC 20007
      </address>
      <address class="address">
        Marlow Crest Tower<br>
        410 Dorsen Avenue #2215<br>
        Miami, FL 33131
      </address>
    </div>
    <p class="web-contact">
      info@civicholdwell.example<br>
      www.civicholdwell.example
    </p>
  </section>
</main>
</body>
</html>
```